Via Lumo K

Need business cards designed. Project is an Arts Center in Hollywood. It'll include 3 live theatre, a restaurant and event space.

Target Market(s)

Across the board, young and old.

Industry/Entity Type

Entertainment

Contact Information for Business Card

Be creative. This is a creative venture that I'm building.

```html
<!DOCTYPE html>
<html lang="en">
<head>
<meta charset="utf-8">
<title>Via Lumo K — Business Card</title>
<link href="https://fonts.googleapis.com/css2?family=Roboto+Condensed:wght@700&family=Open+Sans:wght@400;600&display=swap" rel="stylesheet">
<style>
  :root {
    --page: #ffffff;
    --card-black: #000000;
    --card-tan: #c6b098;
    --name-tan: #cdb69c;
    --brand-red: #8c1c22;
    --text-dark: #1e1e1e;
    --frame-red: #a3141c;
    --photo-sky: #b9c9d4;
    --photo-building: #dcdcdc;
    --photo-ground: #6f6f68;
  }
  html, body {
    margin: 0;
    padding: 0;
    width: 1200px;
    height: 956px;
    overflow: hidden;
    background: var(--page);
  }
  .canvas {
    position: relative;
    width: 1200px;
    height: 956px;
  }
  .card {
    position: absolute;
    left: 210px;
    top: 200px;
    width: 776px;
    height: 438px;
    background: var(--card-tan);
    border: 1px solid #111;
    box-sizing: border-box;
    overflow: hidden;
  }
  .card__top {
    position: absolute;
    left: 0;
    top: 0;
    width: 100%;
    height: 280px;
    background: var(--card-black);
  }
  .card__brand {
    position: absolute;
    left: 52px;
    top: 70px;
    font-family: "Roboto Condensed", sans-serif;
    font-weight: 700;
    font-size: 40px;
    line-height: 1;
    color: var(--brand-red);
    margin: 0;
  }
  .card__name {
    position: absolute;
    left: 50px;
    top: 208px;
    margin: 0;
    font-family: "Roboto Condensed", sans-serif;
    font-weight: 700;
    font-size: 43px;
    line-height: 1;
    color: var(--name-tan);
  }
  .card__contact {
    position: absolute;
    left: 48px;
    top: 302px;
    margin: 0;
    font-family: "Open Sans", sans-serif;
    font-size: 21px;
    line-height: 27px;
    color: var(--text-dark);
    font-style: normal;
  }
  .card__contact span { display: block; }
  .card__venue-image {
    position: absolute;
    left: 382px;
    top: 67px;
    width: 357px;
    height: 264px;
    box-sizing: border-box;
    border: 4px solid var(--frame-red);
    background: linear-gradient(180deg, var(--photo-sky) 0%, var(--photo-building) 45%, var(--photo-building) 70%, var(--photo-ground) 100%);
  }
  .corner-brand {
    position: absolute;
    left: 1048px;
    top: 856px;
    margin: 0;
    font-family: "Roboto Condensed", sans-serif;
    font-weight: 700;
    font-size: 30px;
    line-height: 1;
    color: var(--text-dark);
  }
</style>
</head>
<body>
  <main class="canvas">
    <section class="card">
      <div class="card__top"></div>
      <p class="card__brand">Via Lumo K</p>
      <h1 class="card__name">Daniel Ferrow</h1>
      <address class="card__contact">
        <span>323.555.0147</span>
        <span>dferrow@vialumok.com</span>
        <span>Via Lumo K</span>
        <span>412 N. Larkspur Ave. Los Angeles, CA 90038</span>
      </address>
      <div class="card__venue-image" role="img" aria-label="Architectural rendering of the arts center building with a restaurant, outdoor patio seating and palm trees"></div>
    </section>
    <p class="corner-brand">Via Lumo K</p>
  </main>
</body>
</html>
```